Steelcrest Process Systems. Needs a Business Card Design

We need a business card design for an engineering company which supplies industrial components (pumps, compressors, mechanical seals) provides repairs and services for above mentioned equipments. We offer a uniqe engineering solutions which help our customers to increase the productivness of their manufacturings, and energy savings.

Target Market(s)

Chemical and energy plants, refineries. Food industry and private consumers in a less.

Industry/Entity Type

Business

Contact Information for Business Card

Stylish and sleek design oriented on industrial area.

Requirements
Should not have
• company name shortening

```html
<!DOCTYPE html>
<html lang="en">
<head>
<meta charset="utf-8">
<title>Steelcrest Process Systems — Business Card</title>
<link rel="stylesheet" href="https://fonts.googleapis.com/css2?family=Ubuntu:wght@500&family=Jost:wght@300;400&family=Carlito:ital@1&display=swap">
<style>
  :root {
    --frame-light: #e6e6e6;
    --frame-edge: #9a9a9a;
    --stage: #283845;
    --brand-blue: #1b3aa6;
    --band-blue: #1a38a3;
    --white: #ffffff;
    --steel-light: #f2f2f2;
    --steel-mid: #c9c9c9;
    --steel-dark: #9e9e9e;
  }
  * { margin: 0; padding: 0; box-sizing: border-box; }
  html, body { width: 1200px; height: 1155px; overflow: hidden; }
  body { background: var(--frame-light); position: relative; }

  .stage {
    position: absolute; left: 24px; top: 24px; width: 1152px; height: 1107px;
    background: var(--stage);
    box-shadow: 0 0 0 2px var(--frame-edge), 0 0 12px rgba(0,0,0,.35);
  }

  .card {
    position: absolute; width: 650px; height: 380px; overflow: hidden;
    box-shadow: 14px 18px 22px rgba(0,0,0,.45);
  }
  .card--front { left: 288px; top: 173px; }
  .card--back  { left: 292px; top: 586px; width: 646px; height: 378px; }

  .steel-surface {
    position: absolute; inset: 0;
    background:
      radial-gradient(ellipse at 55% 40%, var(--steel-light) 0%, var(--steel-mid) 35%, var(--steel-light) 55%, var(--steel-dark) 100%);
  }
  .card--back .steel-surface {
    background: radial-gradient(ellipse at 50% 50%, var(--steel-light) 0%, var(--steel-mid) 30%, var(--steel-light) 55%, var(--steel-dark) 100%);
  }

  .brand {
    position: absolute; left: 37px; top: 50px; display: flex; align-items: center; gap: 16px;
  }
  .brand__dot { width: 52px; height: 52px; border-radius: 50%; background: var(--brand-blue); flex: none; }
  .brand__name {
    font-family: "Ubuntu", sans-serif; font-weight: 500; font-size: 33px;
    color: var(--brand-blue); letter-spacing: -0.2px; white-space: nowrap;
  }

  .band { position: absolute; left: 0; top: 0; width: 650px; height: 380px; }

  .contacts { position: absolute; left: 60px; top: 186px; color: var(--white); }
  .contact-line {
    display: flex; align-items: center; gap: 16px; height: 29px;
    font-family: "Jost", sans-serif; font-weight: 300; font-size: 21px; letter-spacing: .3px;
  }
  .contact-line svg { width: 20px; height: 20px; flex: none; }
  .address {
    margin-top: 20px; font-family: "Carlito", sans-serif; font-style: italic;
    font-size: 17px; line-height: 25px;
  }

  .person { position: absolute; left: 364px; top: 231px; color: var(--white); font-family: "Jost", sans-serif; }
  .person__name { font-weight: 400; font-size: 33px; line-height: 38px; letter-spacing: .5px; }
  .person__title { font-weight: 300; font-size: 17px; margin-left: 5px; margin-top: 2px; letter-spacing: .3px; }
  .person__email { font-weight: 300; font-size: 20px; margin-top: 22px; letter-spacing: .3px; }

  .back-brand {
    position: absolute; inset: 0; display: flex; flex-direction: column;
    align-items: center; justify-content: center; gap: 18px;
  }
  .back-brand__dot { width: 90px; height: 90px; border-radius: 50%; background: var(--brand-blue); }
  .back-brand__name {
    font-family: "Ubuntu", sans-serif; font-weight: 500; font-size: 34px; color: var(--brand-blue);
  }
</style>
</head>
<body>
  <main class="stage">
    <section class="card card--front">
      <div class="steel-surface" role="img" aria-label="Brushed steel texture with circular grain"></div>

      <div class="brand">
        <span class="brand__dot"></span>
        <span class="brand__name">Steelcrest Process Systems</span>
      </div>

      <svg class="band" viewBox="0 0 650 380" aria-hidden="true">
        <polygon points="0,139 650,185 650,380 0,380" fill="var(--band-blue)"/>
      </svg>

      <div class="contacts">
        <div class="contact-line">
          <svg viewBox="0 0 20 20" aria-hidden="true"><path d="M5 3c1 0 2 3 2 4s-2 1-1 3 3 4 4 4 2-2 3-1 3 1 3 2-2 3-3 3C8 18 2 12 2 7c0-2 2-4 3-4z" fill="none" stroke="#fff" stroke-width="1.5"/></svg>
          <span>057 400 12 34</span>
        </div>
        <div class="contact-line">
          <svg viewBox="0 0 20 20" aria-hidden="true"><rect x="2" y="8" width="16" height="9" fill="none" stroke="#fff" stroke-width="1.5"/><rect x="6" y="3" width="8" height="5" fill="none" stroke="#fff" stroke-width="1.5"/><rect x="5" y="11" width="4" height="3" fill="#fff"/></svg>
          <span>057 400 56 78</span>
        </div>
        <div class="contact-line">
          <svg viewBox="0 0 20 20" aria-hidden="true"><g fill="none" stroke="#fff" stroke-width="1.3"><circle cx="10" cy="10" r="8"/><ellipse cx="10" cy="10" rx="3.5" ry="8"/><path d="M2 10h16M3.5 6h13M3.5 14h13"/></g></svg>
          <span>STEELCREST.EXAMPLE</span>
        </div>
        <p class="address">вул. Заводська, 12,<br>Харків, Україна, 61000</p>
      </div>

      <div class="person">
        <p class="person__name">YOUR NAME</p>
        <p class="person__title">YOUR TITLE</p>
        <p class="person__email">email@website.com</p>
      </div>
    </section>

    <section class="card card--back">
      <div class="steel-surface" role="img" aria-label="Brushed steel texture with circular grain"></div>
      <div class="back-brand">
        <span class="back-brand__dot"></span>
        <span class="back-brand__name">Steelcrest Process Systems</span>
      </div>
    </section>
  </main>
</body>
</html>
```